Two Separate Canvas Posters 54"width x 36" Height

I need two (2) posters designed for a new restaurant concept called: Lumar Crisp Wrap Kitchen.
Both posters will be printed on Canvas and placed into our new restaurants dining area.
I want this to look hip and cool.
I want so see red colors and earth tones. Please see attached for some ideas that I have.
The final design should communicate that you really gotta have this product and that this is a fun and casual place for a quick bite on the go.
Poster 1 message: gotta Eatta pita!
Size: 54"width x 36" high
Idea: Please see attached for design ideas and colors that I would like to see. If you can come up with any better idea, I would love to see this.
Poster 2 message: Power to the Pita
Size: 54"width x 36" height
Idea: Please see attached for design idea and colors that I want to see.
Restaurant

```html
<!DOCTYPE html>
<html lang="en">
<head>
<meta charset="utf-8">
<title>Power to the Pita</title>
<link rel="stylesheet" href="https://fonts.googleapis.com/css2?family=Anton&family=Oswald:wght@600&display=swap">
<style>
  :root {
    --brick-deep: #5e1710;
    --brick: #7d2416;
    --clay: #9b3a1c;
    --cream: #f0dcb2;
    --mustard: #d9a441;
    --terracotta: #e07a3c;
  }
  html, body {
    margin: 0;
    padding: 0;
    width: 1200px;
    height: 800px;
    overflow: hidden;
    background: var(--brick-deep);
  }
  .poster {
    position: relative;
    width: 1200px;
    height: 800px;
    overflow: hidden;
  }
  .poster-backdrop {
    position: absolute;
    inset: 0;
    background: radial-gradient(ellipse at 50% 50%, var(--clay) 0%, var(--brick) 45%, var(--brick-deep) 100%);
  }
  .poster-art {
    position: absolute;
    inset: 0;
    width: 1200px;
    height: 800px;
  }
  .frame {
    fill: none;
    stroke: var(--cream);
    stroke-width: 3;
    opacity: 0.55;
  }
  .headline {
    font-family: "Anton", "Impact", sans-serif;
    text-anchor: middle;
  }
  .headline-power { font-size: 280px; fill: var(--cream); }
  .headline-pita { font-size: 320px; fill: var(--mustard); }
  .connector {
    font-family: "Oswald", "Arial Narrow", sans-serif;
    font-weight: 600;
    font-size: 52px;
    letter-spacing: 10px;
    fill: var(--terracotta);
    text-anchor: middle;
  }
  .connector-rule {
    stroke: var(--terracotta);
    stroke-width: 4;
  }
</style>
</head>
<body>
  <main class="poster">
    <div class="poster-backdrop"></div>
    <svg class="poster-art" viewBox="0 0 1200 800" xmlns="http://www.w3.org/2000/svg" role="img" aria-label="Power to the Pita">
      <rect class="frame" x="30" y="30" width="1140" height="740"/>
      <text class="headline headline-power" x="600" y="300" textLength="760" lengthAdjust="spacingAndGlyphs">POWER</text>
      <line class="connector-rule" x1="220" y1="385" x2="470" y2="385"/>
      <text class="connector" x="600" y="404" textLength="210" lengthAdjust="spacingAndGlyphs">TO THE</text>
      <line class="connector-rule" x1="730" y1="385" x2="980" y2="385"/>
      <text class="headline headline-pita" x="600" y="725" textLength="640" lengthAdjust="spacingAndGlyphs">PITA</text>
    </svg>
  </main>
</body>
</html>
```